Copper Ridge Garage Door Sales & Repair needs a Business Card Design

I need a business card design to go with our new business logo that was created a few months ago.

Copper Ridge Garage Door specializes in selling and installing new garage doors, and new garage door openers. We also take care of all repairs to existing garage doors and garage door openers. All makes and models.

Target Market(s)

Home-owners, renters, anyone who lives in a house and has a garage. Residential and commercial garages.

Industry/Entity Type

Home Improvement

Contact Information for Business Card

I would like the business cards to have rounded corners and be double-sided. My old logo is still on my website at www.copperridgegarage.example. If I was going to incorporate a secondary color on the business cards, I think that orange is a good choice (especially since blue and orange are the colors of our Tulsa Kestrels), but I'm not opposed to seeing a different color if another color works better with my logo colors. I have two logo colors. One designed for a white background and one designed for a darker background. I'm not opposed to using both. Maybe a dark background with the white logo on one side, and a white background with the other logo color on the other side.

My business is a small, locally owned business that I am trying to grow. But I would like my business cards to look very professional. Like we have been in business for a long time. I like traditional to modern looking cards. Just something bold and memorable. My full company name is Copper Ridge Garage Door Sales & Repair. But you can just do COPPER RIDGE GARAGE DOOR, if that works better.

Font styles to use
Serif
Script

Requirements
Must have
• Rounded corners
• Double-sided
• 3-D Elements. Layering of some sort (a sketch of a garage door or a 3rd color (orange) brought in some how. I really like watermarks.
• Matte cards that you can write on.
• White on one side. (Or the lighter blue in my logo). Darker blue logo color on the other side.
• I would like our tag line on the cards somewhere... "For All Your Garage Door Needs".
• I would also like "Call For a FREE Estimate" by the phone number.
• And "Serving the Greater Metro Denver Area" somewhere on the card as well.
Nice to have
• Refer to "Business Card Details" above.

```html
<!DOCTYPE html>
<html lang="en">
<head>
<meta charset="utf-8">
<title>Copper Ridge Garage Door – Business Card</title>
<link rel="stylesheet" href="https://fonts.googleapis.com/css2?family=Libre+Baskerville:wght@400;700&family=Open+Sans:ital,wght@0,400;0,600;1,600&display=swap">
<style>
  :root {
    --navy: #3f4d73;
    --sky: #b8c9d9;
    --sky-light: #c6d4e2;
    --white: #ffffff;
    --backdrop: #e9e6e1;
    --serif: "Libre Baskerville", Georgia, serif;
    --sans: "Open Sans", Arial, sans-serif;
  }
  * { box-sizing: border-box; margin: 0; padding: 0; }
  html, body { width: 1200px; height: 950px; overflow: hidden; }
  body {
    background: var(--backdrop);
    display: flex;
    align-items: center;
    justify-content: center;
    gap: 100px;
  }
  .card {
    width: 400px;
    height: 700px;
    border-radius: 34px;
    overflow: hidden;
    position: relative;
    box-shadow: 0 8px 24px rgba(0,0,0,.18);
  }

  /* Front */
  .card--front { background: var(--white); }
  .front__band {
    position: absolute;
    top: 0; bottom: 0;
    left: 62px; right: 62px;
    background: var(--navy);
    color: var(--white);
    display: flex;
    flex-direction: column;
    align-items: center;
    text-align: center;
    padding-top: 70px;
  }
  .brand-name {
    font-family: var(--serif);
    font-weight: 700;
    font-size: 30px;
    line-height: 1.15;
    letter-spacing: 1px;
    color: var(--white);
    width: 230px;
  }
  .person { margin-top: 110px; }
  .person__name {
    font-family: var(--serif);
    font-size: 24px;
    letter-spacing: 1px;
  }
  .person__title {
    font-family: var(--serif);
    font-size: 16px;
    margin-top: 4px;
  }
  .contact {
    margin-top: 22px;
    font-family: var(--sans);
    font-size: 15px;
    line-height: 1.6;
  }
  .service-area {
    margin-top: 26px;
    font-family: var(--sans);
    font-style: italic;
    font-weight: 600;
    font-size: 16px;
    line-height: 1.5;
  }

  /* Back */
  .card--back { background: var(--navy); color: var(--white); }
  .estimate {
    position: absolute;
    top: 120px; left: 0; right: 0;
    text-align: center;
    font-family: var(--sans);
  }
  .estimate__label { font-size: 24px; }
  .estimate__phone { font-size: 46px; font-weight: 600; letter-spacing: 1px; margin-top: 2px; }
  .scenery {
    position: absolute;
    left: 0; right: 0; bottom: 0;
    height: 240px;
    background: linear-gradient(180deg, var(--sky-light) 0%, var(--sky) 100%);
  }
  .tagline {
    position: absolute;
    left: 0; right: 0; bottom: 60px;
    text-align: center;
    font-family: var(--sans);
    font-weight: 600;
    font-size: 17px;
    line-height: 1.4;
    color: var(--white);
    letter-spacing: .5px;
  }
</style>
</head>
<body>

  <section class="card card--front">
    <div class="front__band">
      <div class="brand-name">COPPER RIDGE GARAGE DOOR</div>
      <div class="person">
        <div class="person__name">DALE HARPER</div>
        <div class="person__title">CEO/Founder</div>
      </div>
      <div class="contact">
        <div>555-014-2290</div>
        <div>info@copperridgegarage.example</div>
        <div>www.copperridgegarage.example</div>
      </div>
      <div class="service-area">Serving the Greater Metro<br>Denver Area</div>
    </div>
  </section>

  <section class="card card--back">
    <div class="estimate">
      <div class="estimate__label">Call For a FREE Estimate</div>
      <div class="estimate__phone">555-014-2290</div>
    </div>
    <div class="scenery" role="img" aria-label="Illustration of a light blue mountain landscape with a house and garage"></div>
    <div class="tagline">For All Your<br>Garage Door Needs</div>
  </section>

</body>
</html>
```